Custom Header Designs - Automotive Parts - Alternator & Starter

We need 8 Header/Hero designs that will be used on our website. We are a company based in Montreal Canada and we re-manufacture Alternators and Starters for all types of vehicles. We offer a premium product and we are looking for premium designs that reflect the look of our packaging and the look of our website. Essentially we specialize in the sale and manufacture of two specific parts that go on all types of vehicles, Alternators and Starters. All text on these designs need to be editable as we will need to translate them to French once we get the source files.
Here are some websites of our competitors so you can draw some inspiration and see what our industry/business is all about:
https://www.qelvorparts.com/
https://www.zentrihaul.com/
Article that describes a remanufactured product, https://www.wombrixo.com/articles/starters-and-alternators-reman-vs-new.html
Our packaging is modern, sleek and professional. Our website is a B2B E-Commerce Site as well as an info site to promote our products. It is clean and minimal but we want the header/hero designs to help it stand out. Our main colors are blue and gray (as seen in our logo), but you can use whatever you like to compliment these colors.
Our packaging design was done on PixelTroupe, here is the link to that project so that you can see the packaging look and use any of the info that is from that project.
https://jobs.pixeltroupe.ca/job/5829463
The 8 Header/Hero designs will be used in the following areas, I have included a brief description of what we are looking for:
1 - Homepage Header/Hero image - This will be the homepage hero image therefore it should summarize the info described below. We offer premium quality re-manufactured alternators and starters. We are a wholesaler/distributor that services major auto-part stores with these quality products.
2 - General Product Header/Hero image - This image will be used as a header where the customer can learn general info about our products and any custom work we can do. This page will have a section where you can click to learn more about our individual product lines (links to product specific pages mentioned below) and a description of the custom work we can perform. We offer a two year manufacturers warranty.
3 - Alternator Product Header/Hero image - This image will be used to showcase our Alternator Product Line. Its purpose is to promote and advertise our premium re-manufactured alternators. This page will provide detailed info about our alternator re-manufacturing process and describe why our alternators are great.
4 - Starter Product Header/Hero image - This image will be used to showcase our Starter Product Line. Its purpose is to promote and advertise our premium re-manufactured starters. This page will provide detailed info about our starter re-manufacturing process and describe why our starters are great.
5 - General Header/Hero Image - This image will be used in most of our standard pages like our terms and conditions, privacy policy, warranty policy, our company page, etc. It needs to relate to the industry but be general enough so that we could use it in multiple areas
6 - Online Ordering Header image - This image will be used in our B2B area to introduce our customers to the Online Ordering system, its purpose is to advertise and explain some of the features of the Online Ordering system.
7 - B/O Re-Manufacture & Return Header Image - This image will be used in our B2B area to explain and advertise to our customers how our Backorder/R&R process works on our website. Essentially if we do not have the remanufactured part in stock but we have the core you could put the product on Backorder and we will remanufacture it in a few hours. If for any reason (rare vehicle, old vehicle, etc.) we do not have the core we will R&R (Remanufacture and Return) the customers core for them.
8 - Bulk Ordering Form Header Image - This image will be used in our B2B area to explain and advertise to our customers how our Bulk Ordering Form works on our website.
These hero/header images will be going on a Plankly/TillNest website and I am suggesting these images have a size of 1600 x 500, but we will take any other suggestions from the designers as you are the experts.
I have included a zip file that includes images of various elements that will help you in the design process.
Target Market(s)
Educate consumers about our products and attract auto supply chains to become distributors of our products.
Industry/Entity Type
Automotive Part

```html
<!DOCTYPE html>
<html lang="en">
<head>
<meta charset="utf-8">
<title>Korvane Hero Headers</title>
<link href="https://fonts.googleapis.com/css2?family=Roboto:wght@500;700;900&display=swap" rel="stylesheet">
<style>
  :root {
    --navy: #14288c;
    --royal: #10299a;
    --ink: #1b1b1d;
    --white: #ffffff;
    --paper: #ffffff;
    --light-panel: #e8e8ea;
    --dark-panel: #242427;
    --steel-light: #d9dbdf;
    --steel-mid: #9a9da4;
    --steel-dark: #4a4c52;
    --box-light: #2f47a8;
    --box-dark: #0c1858;
  }
  * { box-sizing: border-box; margin: 0; padding: 0; }
  html, body { width: 1200px; height: 3110px; overflow: hidden; }
  body { position: relative; background: var(--paper); font-family: "Roboto", Arial, sans-serif; }

  .brand { position: absolute; display: flex; align-items: center; gap: 14px; }
  .brand-dot { border-radius: 50%; flex: none; }
  .brand-name { font-family: "Roboto", Arial, sans-serif; font-weight: 900; letter-spacing: -1px; line-height: 1; }

  .hero { position: absolute; overflow: hidden; }
  .hero-copy { position: absolute; font-weight: 500; }
  .cta {
    position: absolute; display: flex; align-items: center; justify-content: center; gap: 8px;
    border-radius: 999px; font-weight: 700;
  }
  .cta svg { flex: none; }
  .photo { position: absolute; }
  .box-art { position: absolute; left: 0; top: 0; }

  /* top brand */
  .sheet-brand { left: 400px; top: 108px; }
  .sheet-brand .brand-dot { width: 70px; height: 70px; background: var(--navy); }
  .sheet-brand .brand-name { font-size: 74px; color: var(--navy); }

  /* hero: dark preview */
  .hero-preview { left: 211px; top: 330px; width: 761px; height: 450px;
    background: linear-gradient(180deg, #2a2a2e 0%, #333338 55%, #1f1f22 100%); }
  .hero-preview .brand { left: 57px; top: 128px; gap: 8px; }
  .hero-preview .brand-dot { width: 40px; height: 40px; background: var(--royal); }
  .hero-preview .brand-name { font-size: 40px; color: var(--white); }
  .hero-preview .hero-copy { left: 57px; top: 218px; width: 272px; font-size: 11px; line-height: 19px; color: var(--white); }
  .hero-preview .cta { left: 57px; top: 294px; width: 122px; height: 32px; font-size: 11px; background: var(--royal); color: var(--white); }
  .hero-preview .photo { left: 353px; top: 78px; width: 324px; height: 324px; border-radius: 50%;
    background: radial-gradient(circle at 38% 52%, var(--steel-light) 0%, var(--steel-mid) 45%, var(--steel-dark) 85%, #6d7aa8 100%); }

  /* hero: light */
  .hero-light { left: 64px; top: 976px; width: 1065px; height: 630px; background: var(--light-panel); box-shadow: 0 4px 14px rgba(0,0,0,.18); }
  .hero-light .brand { left: 104px; top: 88px; }
  .hero-light .brand-dot { width: 78px; height: 78px; background: var(--navy); }
  .hero-light .brand-name { font-size: 74px; color: var(--navy); }
  .hero-light .hero-copy { left: 112px; top: 222px; width: 380px; font-size: 16px; line-height: 27px; color: var(--ink); }
  .hero-light .cta { left: 112px; top: 328px; width: 171px; height: 45px; font-size: 16px; background: var(--navy); color: var(--white); }

  /* hero: blue */
  .hero-blue { left: 64px; top: 1682px; width: 1065px; height: 629px; background: var(--royal); }
  .hero-blue .brand { left: 50%; top: 62px; transform: translateX(-50%); }
  .hero-blue .brand-dot { width: 78px; height: 78px; background: var(--white); }
  .hero-blue .brand-name { font-size: 74px; color: var(--white); }
  .hero-blue .tagline { position: absolute; left: 0; right: 0; top: 200px; text-align: center; font-size: 23px; font-weight: 500; color: var(--white); padding-right: 50px; }
  .hero-blue .cta { left: 447px; top: 262px; width: 171px; height: 45px; font-size: 16px; background: var(--white); color: var(--royal); }
  .hero-blue .photo-starter { left: -30px; top: -30px; width: 250px; height: 268px; border-radius: 0 0 60% 40% / 0 0 55% 45%;
    background: linear-gradient(135deg, var(--steel-light) 0%, var(--steel-mid) 55%, var(--steel-dark) 100%); }
  .hero-blue .photo-alternator { left: 866px; top: -20px; width: 230px; height: 258px; border-radius: 50% 0 0 50% / 50% 0 0 50%;
    background: radial-gradient(circle at 35% 60%, #2a2a2e 0 22%, var(--steel-light) 30%, var(--steel-mid) 65%, var(--steel-dark) 100%); }

  /* hero: dark */
  .hero-dark { left: 64px; top: 2388px; width: 1065px; height: 630px;
    background: linear-gradient(180deg, #29292d 0%, #343439 55%, #202023 100%); }
  .hero-dark .brand { left: 80px; top: 184px; gap: 10px; }
  .hero-dark .brand-dot { width: 60px; height: 60px; background: var(--royal); }
  .hero-dark .brand-name { font-size: 60px; color: var(--white); }
  .hero-dark .hero-copy { left: 80px; top: 296px; width: 380px; font-size: 16px; line-height: 27px; color: var(--white); }
  .hero-dark .cta { left: 80px; top: 412px; width: 171px; height: 45px; font-size: 16px; background: var(--royal); color: var(--white); }
  .hero-dark .photo { left: 482px; top: 138px; width: 468px; height: 468px; border-radius: 50%;
    background: radial-gradient(circle at 38% 52%, var(--steel-light) 0%, var(--steel-mid) 45%, var(--steel-dark) 85%, #6d7aa8 100%); }
</style>
</head>
<body>

<div class="brand sheet-brand"><span class="brand-dot"></span><span class="brand-name">Korvane</span></div>

<section class="hero hero-preview">
  <div class="photo" role="img" aria-label="Close-up photo of a remanufactured alternator in a circular frame"></div>
  <div class="brand"><span class="brand-dot"></span><span class="brand-name">Korvane</span></div>
  <p class="hero-copy">Lorem ipsum dolor sit amet, consectetur adipiscing elit, sed do eiusmod tempor incididunt ut labore et dolore magna aliqua</p>
  <a class="cta">Get Started
    <svg width="11" height="11" viewBox="0 0 16 16"><circle cx="8" cy="8" r="8" fill="currentColor"/><path d="M6 4.5 9.5 8 6 11.5" stroke="#10299a" stroke-width="2.2" fill="none"/></svg>
  </a>
</section>

<section class="hero hero-light">
  <svg class="box-art" width="1065" height="630" viewBox="0 0 1065 630">
    <defs>
      <linearGradient id="boxFillLight" x1="0" y1="0" x2="1" y2="1">
        <stop offset="0" stop-color="var(--box-light)"/><stop offset="1" stop-color="var(--box-dark)"/>
      </linearGradient>
    </defs>
    <polygon role="img" aria-label="Alternator product box with packaging artwork" points="448,310 676,260 764,338 764,518 578,610 470,494" fill="url(#boxFillLight)"/>
    <polygon role="img" aria-label="Second alternator product box with packaging artwork" points="772,272 890,206 1038,278 1038,416 896,476 772,416" fill="url(#boxFillLight)"/>
  </svg>
  <div class="brand"><span class="brand-dot"></span><span class="brand-name">Korvane</span></div>
  <p class="hero-copy">Lorem ipsum dolor sit amet, consectetur adipiscing elit, sed do eiusmod tempor incididunt ut labore et dolore magna aliqua</p>
  <a class="cta">Get Started
    <svg width="14" height="14" viewBox="0 0 16 16"><circle cx="8" cy="8" r="8" fill="currentColor"/><path d="M6 4.5 9.5 8 6 11.5" stroke="#14288c" stroke-width="2.2" fill="none"/></svg>
  </a>
</section>

<section class="hero hero-blue">
  <div class="photo photo-starter" role="img" aria-label="Photo of a starter motor"></div>
  <div class="photo photo-alternator" role="img" aria-label="Photo of an alternator pulley"></div>
  <svg class="box-art" width="1065" height="629" viewBox="0 0 1065 629">
    <defs>
      <linearGradient id="boxFillBlue" x1="0" y1="0" x2="1" y2="1">
        <stop offset="0" stop-color="#3a55c0"/><stop offset="1" stop-color="#0a1548"/>
      </linearGradient>
    </defs>
    <polygon role="img" aria-label="Alternator product box with packaging artwork" points="296,394 500,346 584,420 584,586 420,629 330,629 320,574" fill="url(#boxFillBlue)"/>
    <polygon role="img" aria-label="Second alternator product box with packaging artwork" points="588,334 704,298 826,340 826,478 674,538 588,490" fill="url(#boxFillBlue)"/>
  </svg>
  <div class="brand"><span class="brand-dot"></span><span class="brand-name">Korvane</span></div>
  <p class="tagline">Alternators and starters Durable Performance</p>
  <a class="cta">Get Started
    <svg width="14" height="14" viewBox="0 0 16 16"><circle cx="8" cy="8" r="8" fill="currentColor"/><path d="M6 4.5 9.5 8 6 11.5" stroke="#ffffff" stroke-width="2.2" fill="none"/></svg>
  </a>
</section>

<section class="hero hero-dark">
  <div class="photo" role="img" aria-label="Close-up photo of a remanufactured alternator in a circular frame"></div>
  <div class="brand"><span class="brand-dot"></span><span class="brand-name">Korvane</span></div>
  <p class="hero-copy">Lorem ipsum dolor sit amet, consectetur adipiscing elit, sed do eiusmod tempor incididunt ut labore et dolore magna aliqua</p>
  <a class="cta">Get Started
    <svg width="14" height="14" viewBox="0 0 16 16"><circle cx="8" cy="8" r="8" fill="currentColor"/><path d="M6 4.5 9.5 8 6 11.5" stroke="#10299a" stroke-width="2.2" fill="none"/></svg>
  </a>
</section>

</body>
</html>
```